Welding Fabrication and Inspection Business Card Design

Welding Fabrication and Inspection Services,

Business

Industrial Machinery ServicesMohammed Rahim30 Ballarat Street, Mount Gravatt East.4122.QLD

```html
<!DOCTYPE html>
<html lang="en">
<head>
<meta charset="utf-8">
<title>Tarnwell Forge Services – Business Card</title>
<link rel="stylesheet" href="https://fonts.googleapis.com/css2?family=Open+Sans:wght@400;700&display=swap">
<style>
  :root {
    --backdrop: #ecebe8;
    --card-dark: #231f20;
    --card-light: #ffffff;
    --ink: #1f1b1c;
    --ink-soft: #222;
    --paper: #ffffff;
    --rule: #2a2a2a;
  }
  * { margin: 0; padding: 0; box-sizing: border-box; }
  html, body {
    width: 1189px; height: 1200px; overflow: hidden;
    background: var(--backdrop);
    font-family: "Open Sans", Arial, sans-serif;
  }
  .canvas { position: relative; width: 1189px; height: 1200px; }
  .card {
    position: absolute; left: 166px; width: 856px; height: 487px;
    border-radius: 28px; overflow: hidden;
  }
  .card--front { top: 68px; background: var(--card-dark); }
  .card--back { top: 627px; background: var(--card-light); box-shadow: 0 0 0 1px #d8d6d2; }

  .brand-name {
    font-weight: 700; white-space: nowrap;
    display: flex; align-items: center; gap: 14px;
  }
  .brand-mark { border-radius: 50%; flex: none; }

  .card--front .brand-name {
    position: absolute; left: 0; right: 0; top: 208px;
    justify-content: center;
    font-size: 42px; color: var(--paper); letter-spacing: 0.3px;
  }
  .card--front .brand-mark { width: 22px; height: 22px; background: var(--paper); }

  .card--back .brand-name {
    position: absolute; left: 38px; width: 350px; top: 196px;
    justify-content: center;
    font-size: 27px; color: var(--ink);
  }
  .card--back .brand-mark { width: 16px; height: 16px; background: var(--ink); }

  .divider {
    position: absolute; left: 425px; top: 126px; width: 1.5px; height: 241px;
    background: var(--rule);
  }
  .contact { position: absolute; left: 467px; top: 130px; color: var(--ink-soft); }
  .contact__name { font-size: 28px; font-weight: 700; color: var(--ink); line-height: 1.2; }
  .contact__address { margin-top: 34px; font-size: 22.5px; line-height: 30px; }
  .contact__list { list-style: none; margin-top: 14px; font-size: 22.5px; }
  .contact__item { display: flex; align-items: center; gap: 14px; height: 31px; }
  .contact__icon { width: 27px; height: 27px; flex: none; }
</style>
</head>
<body>
<main class="canvas">
  <section class="card card--front" aria-label="Card front">
    <div class="brand-name"><span class="brand-mark"></span>Tarnwell Forge Services</div>
  </section>

  <section class="card card--back" aria-label="Card back">
    <div class="brand-name"><span class="brand-mark"></span>Tarnwell Forge Services</div>
    <div class="divider"></div>
    <div class="contact">
      <p class="contact__name">Khalid Nasser</p>
      <p class="contact__address">17 Corrowen Street,<br>Harlow Vale East. 4190.QLD</p>
      <ul class="contact__list">
        <li class="contact__item">
          <svg class="contact__icon" viewBox="0 0 27 27" aria-hidden="true">
            <rect width="27" height="27" rx="4" fill="#1f1b1c"/>
            <path d="M9 6.5c1 0 2.5 3 2.3 4-.2.8-1.5 1-1.3 2 .4 1.7 1.8 3.6 3.2 4.4.8.4 1.5-.8 2.3-.8 1 0 3.4 2 3.2 3-.3 1.2-2 1.8-3.2 1.6-4-.7-8.2-6.3-8.2-10.6 0-1.5 .8-3.6 1.9-3.6z" fill="#fff"/>
          </svg>
          <span>000-000-0000</span>
        </li>
        <li class="contact__item">
          <svg class="contact__icon" viewBox="0 0 27 27" aria-hidden="true">
            <rect width="27" height="27" rx="4" fill="#1f1b1c"/>
            <rect x="5" y="8" width="17" height="12" fill="#fff"/>
            <path d="M5 8l8.5 7L22 8M5 20l6-6M22 20l-6-6" stroke="#1f1b1c" stroke-width="1.3" fill="none"/>
          </svg>
          <span>khalid@tarnwellforge.com</span>
        </li>
      </ul>
    </div>
  </section>
</main>
</body>
</html>
```